Korvane Associates Inc. - Cyber security company needs web site redesign

Need to redesign the corporate web page. Static content with no rss feeds. Web page is for basic marketing and corporate information. KAI is a management and cyber security consulting firm. The company logo has been redesigned and would like to incorporate this new logo into the design. Also need to reference MADE IN USA logo, SDVOSB logo, Include the current content from the existing web page and will revise as needed
Updates

Target Market(s)

Government and Commercial Clients and potential new employees

Industry/Entity Type

It Company

Number of Pages Required

1 page

Font styles to use
Sans Serif

Requirements
Must have
• New Korvane Associates Logo
• MADE IN USA logo
• SDVOSB logo
• Cyber security theme
Nice to have
• animation
• Cyber security related graphics
Should not have
• Search and News sections

```html
<!DOCTYPE html>
<html lang="en">
<head>
<meta charset="utf-8">
<title>Korvane Associates Inc.</title>
<link href="https://fonts.googleapis.com/css2?family=Open+Sans:wght@300;400;600;700&family=Arimo:wght@400;700&display=swap" rel="stylesheet">
<style>
:root{
  --red:#e30613;
  --ink:#333333;
  --muted:#777777;
  --charcoal:#3a3a3a;
  --footer:#1b1b1b;
  --footer-bar:#0c0c0c;
  --paper:#ffffff;
  --mist:#f4f4f4;
  --line:#555555;
  --blue:#1565c0;
  --navy:#1a3f7a;
}
*{box-sizing:border-box;margin:0;padding:0}
html,body{width:1200px;height:2715px;overflow:hidden;background:var(--paper)}
body{font-family:"Arimo",Arial,sans-serif;color:var(--ink);position:relative}
h1,h2,h3{font-weight:400}
.abs{position:absolute}

/* header */
.site-header{position:absolute;left:0;top:0;width:1200px;height:172px;background:var(--paper)}
.brand{left:100px;top:60px;display:flex;align-items:center;gap:10px}
.brand-mark{width:22px;height:22px;background:var(--red)}
.brand-name{font-family:"Open Sans",sans-serif;font-weight:700;font-size:20px;color:var(--red)}
.phone{left:792px;top:44px;display:flex;align-items:center;gap:10px;font-family:"Open Sans",sans-serif;font-weight:600;font-size:21px;color:var(--ink)}
.login{left:1006px;top:37px;width:90px;height:38px;background:var(--blue);border-radius:3px;color:#fff;font-size:14px;font-weight:700;display:flex;align-items:center;justify-content:center;gap:7px}
.nav{right:100px;top:109px;display:flex;height:38px;align-items:center;gap:56px}
.nav a{font-size:15px;color:var(--ink);text-decoration:none;height:38px;line-height:38px}
.nav .home{background:var(--red);color:#fff;width:90px;text-align:center}

/* hero */
.hero{left:0;top:172px;width:1200px;height:585px;background:linear-gradient(100deg,#23272b 0%,#3c4248 35%,#2a2d31 60%,#0a0a0a 100%)}
.hero-title{left:0;width:1200px;top:475px;text-align:center;font-family:"Open Sans",sans-serif;font-weight:700;font-size:48px;line-height:60px;color:#fff}
.hero-text{left:160px;width:880px;top:553px;text-align:center;font-size:13px;line-height:22px;color:#fff}
.btn{display:inline-block;background:var(--red);color:#fff;font-size:13px;text-align:center;border-radius:2px}
.hero-btn{left:552px;top:619px;width:98px;height:37px;line-height:37px}

/* welcome */
.welcome-title{left:0;width:1200px;top:800px;text-align:center;font-family:"Open Sans",sans-serif;font-weight:400;font-size:38px;line-height:50px;color:var(--ink)}
.welcome-title span{color:var(--red)}
.welcome-text{left:130px;width:940px;top:868px;text-align:center;font-size:13px;line-height:22px;color:var(--muted)}
.card{top:963px;width:290px;height:353px}
.card-photo{height:154px;background:linear-gradient(135deg,#4a3a33,#8a6a56 55%,#d9d2cc)}
.card-body{height:199px;border-bottom-left-radius:50% 70px;border-bottom-right-radius:50% 70px;text-align:center;color:#fff;padding-top:12px}
.card-body.red{background:var(--red)}
.card-body.dark{background:var(--charcoal)}
.card-title{font-family:"Open Sans",sans-serif;font-size:23px;font-weight:600;line-height:30px}
.card-text{font-size:12px;font-weight:700;line-height:19px;padding:6px 16px 0}
.card-btn{margin-top:12px;width:100px;height:33px;line-height:33px;font-weight:700}
.card-btn.black{background:#1a1a1a}

/* why */
.why{left:0;top:1417px;width:1200px;height:366px;background:linear-gradient(90deg,var(--mist),#fafafa 55%,#fff)}
.why-photo{left:660px;top:1417px;width:540px;height:366px;background:linear-gradient(180deg,#f2f2f2,#dfe6ee 45%,#cfd6dd)}
.why-title{left:100px;top:1454px;font-family:"Open Sans",sans-serif;font-weight:400;font-size:31px;line-height:40px;color:var(--ink)}
.why-text{left:105px;top:1507px;width:505px;font-size:13px;line-height:20px;color:var(--muted)}
.value{font-size:13px;color:var(--ink);display:flex;align-items:center;gap:9px}

/* services */
.services-title{left:0;width:1200px;top:1826px;text-align:center;font-family:"Open Sans",sans-serif;font-weight:400;font-size:29px;line-height:38px;color:var(--ink)}
.services-text{left:290px;width:620px;top:1880px;text-align:center;font-size:13px;line-height:22px;color:var(--muted)}
.service h3{font-size:14px;font-weight:400;color:var(--ink);margin-bottom:6px}
.service p{font-size:12px;line-height:19px;color:#999}
.laptop{left:407px;top:2009px;width:402px;height:217px;background:linear-gradient(180deg,#2a2a2a 0 4%,#f7f7f7 4% 88%,#cfcfcf 88%);border-radius:8px 8px 4px 4px}

/* footer */
.footer{left:0;top:2384px;width:1200px;height:291px;background:var(--footer)}
.footer-bar{left:0;top:2675px;width:1200px;height:40px;background:var(--footer-bar);color:#fff;font-size:13px;text-align:center;line-height:40px}
.f-head{font-size:15px;color:#fff;display:flex;align-items:center;gap:18px}
.f-head i{display:block;width:56px;height:1px;background:var(--line)}
.links{list-style:none}
.links li{font-size:13px;color:#fff;line-height:25px;display:flex;align-items:center;gap:10px}
.links li::before{content:"";width:5px;height:5px;border-radius:50%;background:#fff}
.field{width:199px;height:31px;background:#fff;font-size:11px;color:#444;padding:7px 6px}
.submit{width:82px;height:28px;line-height:28px;background:var(--red);color:#fff;font-size:13px;font-weight:700;text-align:center}
.contact-row{display:flex;align-items:flex-start;gap:22px;font-size:13px;line-height:21px;color:#fff}
.footer-brand{left:920px;top:2420px;width:200px;text-align:center;font-family:"Open Sans",sans-serif;font-weight:700;font-size:16px;line-height:22px;color:#9a9a9a}
.badges{left:940px;top:2490px;width:160px;display:flex;justify-content:space-between}
.badge{width:72px;height:72px;border-radius:50%;border:3px solid #9a9a9a}
.badge.usa{background:#2a3550}
.badge.vet{background:#4a2a2a}
.vline{width:1px;background:#2e2e2e}
</style>
</head>
<body>

<header class="site-header">
  <div class="abs brand"><span class="brand-mark"></span><span class="brand-name">Korvane Associates Inc.</span></div>
  <div class="abs phone">
    <svg width="24" height="24" viewBox="0 0 24 24"><circle cx="12" cy="12" r="10" fill="none" stroke="#1565c0" stroke-width="2"/><path d="M8 7c1 0 1.5 2 1.3 2.5L8.7 10.4c.8 1.9 2.3 3.4 4.9 4.9l.9-.6c.5-.2 2.5.3 2.5 1.3 0 1-1 2-2 2C10 18 6 14 6 9c0-1 1-2 2-2z" fill="#1565c0"/></svg>
    (555) 310-4472
  </div>
  <div class="abs login">
    <svg width="14" height="14" viewBox="0 0 14 14"><rect x="1" y="1" width="12" height="12" fill="none" stroke="#fff" stroke-width="1.6"/><path d="M3 7h6M6.5 4.5 9 7 6.5 9.5" stroke="#fff" stroke-width="1.6" fill="none"/></svg>
    Login
  </div>
  <nav class="abs nav">
    <a class="home">Home</a>
    <a>Services</a>
    <a>About Us</a>
    <a>Careers</a>
    <a>Contact Us</a>
  </nav>
</header>

<section class="abs hero" role="img" aria-label="Hand holding a tablet with a network of cyber security terms over a dark server room"></section>
<h1 class="abs hero-title">We Provide Securty major</h1>
<p class="abs hero-text">Sed ut perspiciatis unde omnis iste natus error sit voluptatem accusantium doloremque laudantium, totam rem aperiam, eaque ipsa quae ab illo inventore veritatis et quasi architecto beatae vitae dicta sunt explicabo.</p>
<span class="abs btn hero-btn">Read More</span>

<h2 class="abs welcome-title">Welcome To <span>Korvane Associates Inc</span></h2>
<p class="abs welcome-text">Sed ut perspiciatis unde omnis iste natus error sit voluptatem accusantium doloremque laudantium, totam rem aperiam, eaque ipsa quae ab illo inventore veritatis et quasi architecto beatae vitae dicta sunt explicabo.</p>

<article class="abs card" style="left:103px">
  <div class="card-photo" role="img" aria-label="Hands using a smartphone beside a laptop"></div>
  <div class="card-body red">
    <div class="card-title">What We Do</div>
    <p class="card-text">Sed ut perspiciatis unde omnis iste natus error sit voluptatem accusantium doloremque laudantium, totam rem aperiam, eaque ipsa quae ab illo inventore</p>
    <span class="btn card-btn black">Read More</span>
  </div>
</article>
<article class="abs card" style="left:461px">
  <div class="card-photo" role="img" aria-label="Hands using a smartphone beside a laptop"></div>
  <div class="card-body dark">
    <div class="card-title">Benefit Package</div>
    <p class="card-text">Sed ut perspiciatis unde omnis iste natus error sit voluptatem accusantium doloremque laudantium, totam rem aperiam, eaque ipsa quae ab illo inventore</p>
    <span class="btn card-btn">Read More</span>
  </div>
</article>
<article class="abs card" style="left:807px">
  <div class="card-photo" role="img" aria-label="Hands using a smartphone beside a laptop"></div>
  <div class="card-body dark">
    <div class="card-title">Career</div>
    <p class="card-text">Sed ut perspiciatis unde omnis iste natus error sit voluptatem accusantium doloremque laudantium, totam rem aperiam, eaque ipsa quae ab illo inventore</p>
    <span class="btn card-btn">Read More</span>
  </div>
</article>

<section class="abs why"></section>
<div class="abs why-photo" role="img" aria-label="Smiling man in a blue shirt working at a laptop"></div>
<h2 class="abs why-title">Why Korvane Associates?</h2>
<p class="abs why-text">Sed ut perspiciatis unde omnis iste natus error sit voluptatem accusantium doloremque laudantium, totam rem aperiam, eaque ipsa quae ab illo inventore veritatis et quasi architecto beatae .</p>
<svg width="0" height="0" style="position:absolute"><defs><symbol id="tick" viewBox="0 0 14 14"><rect x="1" y="2" width="11" height="11" fill="none" stroke="#e30613" stroke-width="1.6"/><path d="M3.5 7l2.5 2.5L13 1.5" fill="none" stroke="#e30613" stroke-width="2"/></symbol></defs></svg>
<div class="abs value" style="left:112px;top:1594px"><svg width="14" height="14"><use href="#tick"/></svg>Honor</div>
<div class="abs value" style="left:112px;top:1626px"><svg width="14" height="14"><use href="#tick"/></svg>Loyalty</div>
<div class="abs value" style="left:112px;top:1659px"><svg width="14" height="14"><use href="#tick"/></svg>Bravery</div>
<div class="abs value" style="left:251px;top:1594px"><svg width="14" height="14"><use href="#tick"/></svg>Compassion</div>
<div class="abs value" style="left:251px;top:1626px"><svg width="14" height="14"><use href="#tick"/></svg>Truthfulness</div>
<div class="abs value" style="left:427px;top:1593px"><svg width="14" height="14"><use href="#tick"/></svg>Justice</div>
<div class="abs value" style="left:427px;top:1627px"><svg width="14" height="14"><use href="#tick"/></svg>Respect</div>

<h2 class="abs services-title">Our Services</h2>
<p class="abs services-text">Sed ut perspiciatis unde omnis iste natus error sit voluptatem accusantium doloremque laudantium, totam rem aperiam, eaque ipsa quae ab illo inventore</p>

<svg class="abs" style="left:0;top:1940px" width="1200" height="390" viewBox="0 1940 1200 390">
  <g stroke="#555" stroke-width="2" stroke-dasharray="9 6" fill="none">
    <path d="M382 1976V2262"/><path d="M818 1976V2262"/>
    <path d="M382 1976H335"/><path d="M382 2118H335"/><path d="M382 2262H335"/>
    <path d="M818 1976H868"/><path d="M818 2118H868"/><path d="M818 2262H868"/>
  </g>
  <g stroke="#555" stroke-width="2" fill="none">
    <path d="M382 2118H400"/><circle cx="404" cy="2118" r="4" fill="#fff"/>
    <path d="M818 2118H796"/><circle cx="792" cy="2118" r="4" fill="#fff"/>
  </g>
  <g fill="#555">
    <path d="M332 1976l8-4v8z"/><path d="M332 2118l8-4v8z"/><path d="M332 2262l8-4v8z"/>
    <path d="M872 1976l-8-4v8z"/><path d="M872 2118l-8-4v8z"/><path d="M872 2262l-8-4v8z"/>
  </g>
  <g>
    <circle cx="293" cy="1976" r="30" fill="#e8e8e8"/><circle cx="293" cy="1976" r="24" fill="#1a3f7a"/>
    <circle cx="293" cy="1978" r="8" fill="none" stroke="#fff" stroke-width="2"/><path d="M293 1964v6M281 1978h4M301 1978h4" stroke="#fff" stroke-width="2"/>
    <circle cx="293" cy="2118" r="30" fill="#e8e8e8"/><circle cx="293" cy="2118" r="24" fill="#e30613"/>
    <path d="M286 2110h14l-2 16h-10z" fill="none" stroke="#fff" stroke-width="2"/><path d="M283 2110h20" stroke="#fff" stroke-width="2"/>
    <circle cx="293" cy="2262" r="30" fill="#e8e8e8"/><circle cx="293" cy="2262" r="24" fill="#2b2b2b"/>
    <circle cx="293" cy="2258" r="7" fill="#fff"/><rect x="290" y="2265" width="6" height="6" fill="#fff"/>
    <circle cx="916" cy="1976" r="30" fill="#e8e8e8"/><circle cx="916" cy="1976" r="24" fill="#1a3f7a"/>
    <circle cx="914" cy="1974" r="8" fill="none" stroke="#fff" stroke-width="2.5"/><path d="M920 1980l7 7" stroke="#fff" stroke-width="3"/>
    <circle cx="916" cy="2118" r="30" fill="#e8e8e8"/><circle cx="916" cy="2118" r="24" fill="#e30613"/>
    <circle cx="916" cy="2118" r="11" fill="none" stroke="#fff" stroke-width="2"/><circle cx="916" cy="2118" r="5" fill="none" stroke="#fff" stroke-width="2"/>
    <circle cx="916" cy="2262" r="30" fill="#e8e8e8"/><circle cx="916" cy="2262" r="24" fill="#2b2b2b"/>
    <path d="M916 2250l10 4v6c0 6-4 10-10 12-6-2-10-6-10-12v-6z" fill="none" stroke="#fff" stroke-width="2"/>
  </g>
</svg>
<div class="abs laptop" role="img" aria-label="Laptop displaying the company logo"></div>

<div class="abs service" style="left:99px;top:1957px"><h3>Threat Analysis</h3><p>Lorem ipsum dolor sit<br>amet consectetur..</p></div>
<div class="abs service" style="left:99px;top:2097px"><h3>Threat Mitigation</h3><p>Lorem ipsum dolor sit<br>amet consectetur..</p></div>
<div class="abs service" style="left:99px;top:2241px"><h3>Automated Solutions</h3><p>Lorem ipsum dolor sit<br>amet consectetur..</p></div>
<div class="abs service" style="left:965px;top:1957px"><h3>Malware Analysis</h3><p>Lorem ipsum dolor sit<br>amet consectetur..</p></div>
<div class="abs service" style="left:965px;top:2097px"><h3>Threat Operation</h3><p>Lorem ipsum dolor sit<br>amet consectetur..</p></div>
<div class="abs service" style="left:965px;top:2241px"><h3>Securty Services</h3><p>Lorem ipsum dolor sit<br>amet consectetur..</p></div>

<footer class="abs footer"></footer>
<div class="abs vline" style="left:265px;top:2420px;height:220px"></div>
<div class="abs vline" style="left:565px;top:2420px;height:220px"></div>
<div class="abs f-head" style="left:100px;top:2415px">Quick Links<i></i></div>
<ul class="abs links" style="left:100px;top:2449px">
  <li>Home</li><li>Services</li><li>About Us</li><li>Careers</li><li>Contact Us</li>
</ul>
<div class="abs f-head" style="left:315px;top:2415px">Quick Inquiry<i></i></div>
<div class="abs field" style="left:317px;top:2456px">Name</div>
<div class="abs field" style="left:317px;top:2496px">Email</div>
<div class="abs field" style="left:317px;top:2536px;height:55px">Message</div>
<div class="abs submit" style="left:317px;top:2601px">SUBMIT</div>
<div class="abs f-head" style="left:612px;top:2415px">Contact Details<i></i></div>
<div class="abs contact-row" style="left:608px;top:2456px">
  <svg width="14" height="20" viewBox="0 0 14 20"><path d="M7 1a6 6 0 0 1 6 6c0 5-6 12-6 12S1 12 1 7a6 6 0 0 1 6-6z" fill="#fff"/><circle cx="7" cy="7" r="2.3" fill="#1b1b1b"/></svg>
  <span>2710 Westridge Lane #200<br>Fairview ut5810</span>
</div>
<div class="abs contact-row" style="left:608px;top:2518px">
  <svg width="18" height="16" viewBox="0 0 18 16"><path d="M2 4c4-3 10-3 14 0v3h-4V5H6v2H2z" fill="#fff"/><rect x="3" y="8" width="12" height="7" rx="1" fill="#fff"/></svg>
  <span>555-310-4472</span>
</div>
<div class="abs contact-row" style="left:608px;top:2559px">
  <svg width="18" height="14" viewBox="0 0 18 14"><path d="M1 5l8-4 8 4v8H1z" fill="#fff"/><path d="M1 5l8 5 8-5" fill="none" stroke="#1b1b1b" stroke-width="1.4"/></svg>
  <span>info@korvane-example.com</span>
</div>
<div class="abs footer-brand">Korvane Associates Inc.</div>
<div class="abs badges">
  <div class="badge usa" role="img" aria-label="Made in USA badge"></div>
  <div class="badge vet" role="img" aria-label="Service-disabled veteran-owned small business badge"></div>
</div>
<div class="abs footer-bar">Copyright 2014 All right reserved</div>

</body>
</html>
```